Tranquil Pathway Business Card

Logo attached. (will be printing onto thick white/off white textured card)

Double sided business card for two Therapists working at Tranquil Pathway.

Require one design, but with different name and mobile numbers on each card.

Target Market(s)

Medical, Health

Industry/Entity Type

Business

Contact Information for Business Card

Need one business card design, but a separate card for each person - Colin Marchetti and Marieke de Boeckx.

FRONT OF CARD

Logo

Name (Colin Marchetti on one card, Marieke de Boeckx on the other)
Professional Clinical Hypnotherapist

Consulting Rooms (Near Lindqvist Hospital)
482 Brackenfield Road
Dunmore VIC 3987

Colin@TranquilPathway.example.au OR Marieke@TranquilPathway.example.au

Mobile: 0455 872 604 (for Colin) OR
Mobile: 0467 290 518 (for Marieke)

BACK OF CARD

Logo

Website: www.TranquilPathway.example.au

Phone: 1300 958 471

Requirements
Must have
• Text and logo only. No additiional graphics.

```html
<!DOCTYPE html>
<html lang="en">
<head>
<meta charset="UTF-8">
<title>Tranquil Pathway Business Card</title>
<link rel="stylesheet" href="https://fonts.googleapis.com/css2?family=Questrial&family=Montserrat:wght@700&family=Arimo:wght@400&display=swap">
<style>
  :root {
    --page: #ffffff;
    --card-light: #ececec;
    --card-light-edge: #dcdcdc;
    --band-dark: #4a4a4b;
    --band-glow: #5e5e5f;
    --navy: #2a2f6b;
    --sky: #29abe2;
    --white: #ffffff;
    --shadow: rgba(0, 0, 0, 0.28);
  }
  * { box-sizing: border-box; margin: 0; padding: 0; }
  html, body {
    width: 969px;
    height: 1200px;
    overflow: hidden;
    background: var(--page);
  }
  .canvas {
    position: relative;
    width: 969px;
    height: 1200px;
  }
  .card {
    position: absolute;
    left: 17px;
    width: 839px;
    height: 504px;
    overflow: hidden;
    box-shadow: 14px 22px 40px var(--shadow);
  }
  .card--front { top: 0; background: var(--card-light); }
  .card--back {
    top: 567px;
    background: radial-gradient(ellipse at 50% 45%, #f8f8f8 0%, var(--card-light) 70%, var(--card-light-edge) 100%);
  }

  .brand {
    position: absolute;
    display: flex;
    align-items: center;
  }
  .brand__dot {
    border-radius: 50%;
    background: var(--navy);
    flex: none;
  }
  .brand__name {
    font-family: "Montserrat", sans-serif;
    font-weight: 700;
    color: var(--navy);
    text-transform: uppercase;
    line-height: 1.08;
    letter-spacing: 0.02em;
  }
  .card--front .brand { left: 401px; top: 34px; gap: 30px; }
  .card--front .brand__dot { width: 124px; height: 124px; }
  .card--front .brand__name { font-size: 36px; }
  .card--back .brand { left: 190px; top: 159px; gap: 36px; }
  .card--back .brand__dot { width: 132px; height: 132px; }
  .card--back .brand__name { font-size: 42px; }

  .band {
    position: absolute;
    left: 0;
    top: 197px;
    width: 839px;
    height: 307px;
    background: radial-gradient(ellipse at 40% 25%, var(--band-glow) 0%, var(--band-dark) 60%);
  }
  .person__name {
    position: absolute;
    left: 48px;
    top: 49px;
    font-family: "Questrial", sans-serif;
    font-size: 43px;
    color: var(--sky);
    letter-spacing: 0.01em;
  }
  .person__role {
    position: absolute;
    left: 49px;
    top: 105px;
    font-family: "Questrial", sans-serif;
    font-size: 20px;
    color: var(--white);
  }
  .contact {
    position: absolute;
    right: 32px;
    top: 133px;
    font-family: "Arimo", sans-serif;
    color: var(--white);
    text-align: right;
  }
  .contact__row {
    display: flex;
    justify-content: flex-end;
    align-items: flex-start;
    gap: 12px;
  }
  .contact__icon { width: 30px; flex: none; display: flex; justify-content: center; }
  .contact__phone { font-size: 31px; line-height: 36px; }
  .contact__email { font-size: 19px; line-height: 24px; margin-top: 12px; }
  .contact__address { font-size: 19px; line-height: 21.5px; margin-top: 11px; }

  .back-contact {
    position: absolute;
    left: 0;
    width: 100%;
    top: 422px;
    text-align: center;
    font-family: "Arimo", sans-serif;
    font-size: 22px;
    line-height: 27px;
    color: var(--navy);
  }
</style>
</head>
<body>
<div class="canvas">

  <section class="card card--front">
    <div class="brand">
      <div class="brand__dot"></div>
      <div class="brand__name">Tranquil<br>Pathway</div>
    </div>

    <div class="band">
      <h1 class="person__name">Colin Marchetti</h1>
      <p class="person__role">Professional Clinical Hypnotherapist</p>

      <div class="contact">
        <div class="contact__row contact__phone">
          <span>0455 872 604</span>
          <span class="contact__icon">
            <svg width="30" height="30" viewBox="0 0 30 30" aria-hidden="true">
              <circle cx="15" cy="15" r="13" fill="none" stroke="#fff" stroke-width="2.2"/>
              <path d="M10 8.5c1.2-.8 2 .2 2.6 1.4l.7 1.4c.3.7 0 1.3-.6 1.7l-.8.6c.7 1.9 2 3.3 3.9 4.2l.7-.8c.5-.6 1.1-.8 1.8-.4l1.4.8c1.1.6 1.8 1.5.9 2.6-1.1 1.4-3 1.7-4.7.8-3.4-1.7-5.8-4.4-6.9-7.9-.5-1.7-.1-3.5 1-4.4z" fill="#fff"/>
            </svg>
          </span>
        </div>
        <div class="contact__row contact__email">
          <span>Colin@TranquilPathway.example.au</span>
          <span class="contact__icon">
            <svg width="26" height="18" viewBox="0 0 26 18" aria-hidden="true" style="margin-top:4px">
              <rect x="0" y="0" width="26" height="18" fill="#fff"/>
              <path d="M0 0 L13 10 L26 0" fill="none" stroke="#4a4a4b" stroke-width="2"/>
            </svg>
          </span>
        </div>
        <div class="contact__row contact__address">
          <span>Consulting Rooms (Near Lindqvist Hospital)<br>482 Brackenfield Road<br>Dunmore VIC 3987</span>
          <span class="contact__icon">
            <svg width="26" height="26" viewBox="0 0 26 26" aria-hidden="true" style="margin-top:2px">
              <path d="M1 10 L13 2 L25 10 V25 H1 Z" fill="#fff"/>
              <rect x="6" y="14" width="6" height="5" fill="#4a4a4b"/>
              <rect x="15" y="14" width="5" height="11" fill="#4a4a4b"/>
            </svg>
          </span>
        </div>
      </div>
    </div>
  </section>

  <section class="card card--back">
    <div class="brand">
      <div class="brand__dot"></div>
      <div class="brand__name">Tranquil<br>Pathway</div>
    </div>
    <div class="back-contact">
      <p>www.TranquilPathway.example.au</p>
      <p>Phone : 1300 958 471</p>
    </div>
  </section>

</div>
</body>
</html>
```